Inspiring Fundraising Foundation Website to Provide Academic Scholarships

Hello, we are launching a foundation to provide academic scholarships to high school students for college. We'd like this to be an informational website with contact information. There will be a total of approximately 5-7 pages in all.
The color scheme will be purple and white, with a girly feel. I 've attached the logo for reference!

Reason: Extending deadline to go over revisions

Target Market(s)

high school students, college students

Industry/Entity Type

Education

Coding

Coded - Design and coding required

Number of Pages Required

5+ page

Font styles to use
Serif
Sans Serif
Script

Colors
6b449b
886aae
b7a5cd
e4daeb
ffffff
fdf9cf
fbf289

Requirements
Must have
• Purple, girly feel, to reflect the logo's style. Should be light-themed
Should not have
• No dark themes (aka heavy on black or dark colors)

```html
<!DOCTYPE html>
<html lang="en">
<head>
<meta charset="utf-8">
<title>Elena Marlowe Foundation</title>
<link href="https://fonts.googleapis.com/css2?family=Lato:wght@400;700&family=Open+Sans:ital,wght@0,400;0,600;1,400&display=swap" rel="stylesheet">
<style>
  :root {
    --purple-deep: #3a1a55;
    --purple: #6b449b;
    --purple-mid: #886aae;
    --purple-soft: #b7a5cd;
    --lilac: #e4daeb;
    --white: #ffffff;
    --band: #f7f7f7;
    --card: #f6f6f6;
    --text: #7a7a7a;
    --dark: #333333;
    --rule: #d8d8d8;
  }
  * { box-sizing: border-box; margin: 0; padding: 0; }
  html, body { width: 1200px; height: 2256px; overflow: hidden; }
  body { position: relative; background: var(--white); font-family: "Open Sans", Arial, sans-serif; color: var(--text); }
  .abs { position: absolute; }

  /* Header */
  .site-header { position: absolute; left: 0; top: 0; width: 1200px; height: 132px; background: var(--white); }
  .brand { position: absolute; left: 132px; top: 18px; font-family: "Lato", sans-serif; font-weight: 700; color: var(--purple-deep); line-height: 1; }
  .brand .name { font-size: 27px; display: block; line-height: 30px; }
  .brand .sub { font-size: 11px; letter-spacing: 2px; display: block; margin-top: 6px; }
  .social-top { position: absolute; top: 27px; left: 947px; display: flex; gap: 6px; }
  .social-top span { width: 36px; height: 36px; border-radius: 50%; background: var(--purple-mid); display: block; }
  .main-nav { position: absolute; top: 97px; left: 0; width: 1200px; font-family: "Lato", sans-serif; font-size: 12.5px; letter-spacing: 1.3px; color: var(--dark); }
  .main-nav a { position: absolute; color: inherit; text-decoration: none; white-space: nowrap; }
  .main-nav a.active { color: var(--purple); }
  .nav-underline { position: absolute; left: 555px; top: 128px; width: 42px; height: 4px; background: var(--purple); }

  /* Hero */
  .hero { position: absolute; left: 0; top: 132px; width: 1200px; height: 474px;
    background: linear-gradient(90deg, #6f7a62 0%, #8a7c78 25%, #9a8a84 45%, #b8a69b 60%, #d9c2b0 70%, #3fa7b3 85%, #2e8c98 100%); }
  .hero-title { position: absolute; left: 132px; top: 140px; font-family: "Lato", sans-serif; color: var(--white); letter-spacing: 2.5px; text-shadow: 0 1px 3px rgba(0,0,0,.25); }
  .hero-title .l1 { display: block; font-size: 33px; line-height: 44px; }
  .hero-title .l2 { display: block; font-size: 39px; line-height: 46px; }
  .hero-btn { position: absolute; left: 132px; top: 264px; width: 197px; height: 55px; background: var(--purple); color: var(--white); font-family: "Lato", sans-serif; font-size: 16px; letter-spacing: 1.5px; display: flex; align-items: center; justify-content: center; border-radius: 2px; }
  .hero-dots { position: absolute; left: 132px; top: 369px; display: flex; gap: 4px; }
  .hero-dots span { width: 11px; height: 11px; border-radius: 50%; background: rgba(255,255,255,.55); }
  .hero-dots span:first-child { background: var(--white); }

  /* Sections */
  .section-title { position: absolute; left: 0; width: 1200px; text-align: center; font-family: "Lato", sans-serif; font-size: 36px; letter-spacing: 3px; color: var(--purple-deep); }
  .welcome-text { position: absolute; left: 191px; top: 725px; width: 818px; text-align: center; font-size: 11.5px; line-height: 24px; }
  .btn-small { position: absolute; background: var(--purple); color: var(--white); font-family: "Lato", sans-serif; font-size: 11.5px; letter-spacing: 1.3px; display: flex; align-items: center; justify-content: center; border-radius: 2px; }

  .services-band { position: absolute; left: 0; top: 932px; width: 1200px; height: 507px; background: var(--band); }
  .service { position: absolute; top: 1108px; width: 284px; text-align: center; }
  .service svg { display: block; margin: 0 auto; }
  .service h3 { font-family: "Lato", sans-serif; font-weight: 400; font-size: 20px; letter-spacing: 2px; color: var(--purple-deep); margin-top: 32px; }
  .service p { font-size: 11.5px; line-height: 24px; text-align: justify; text-align-last: center; margin-top: 22px; }
  .service .more { display: block; margin-top: 20px; font-family: "Lato", sans-serif; font-size: 11.5px; letter-spacing: 1.2px; color: var(--purple); }

  .testimonial { position: absolute; top: 1587px; width: 456px; height: 215px; background: var(--card); }
  .testimonial p { position: absolute; left: 32px; top: 24px; width: 392px; font-size: 11.5px; line-height: 24px; }
  .testimonial .author { position: absolute; left: 40px; top: 140px; font-style: italic; font-size: 11px; color: var(--purple-deep); }
  .avatar { position: absolute; width: 102px; height: 102px; border-radius: 50%; border: 2px solid var(--purple); background: radial-gradient(circle at 50% 40%, #d8bca7 0%, #a88a78 55%, #7a6a66 100%); }

  /* Footer */
  .site-footer { position: absolute; left: 0; top: 1915px; width: 1200px; height: 341px; background: var(--band); }
  .footer-brand { position: absolute; left: 132px; top: 1972px; font-family: "Lato", sans-serif; font-weight: 700; color: var(--purple-deep); }
  .footer-brand .name { display: block; font-size: 30px; line-height: 34px; }
  .footer-brand .sub { display: block; font-size: 11px; letter-spacing: 2.5px; margin-top: 8px; }
  .social-foot { position: absolute; left: 134px; top: 2103px; display: flex; gap: 7px; }
  .social-foot span { width: 30px; height: 30px; border-radius: 50%; border: 1.5px solid var(--dark); display: block; }
  .footer-heading { position: absolute; top: 1964px; font-family: "Lato", sans-serif; font-size: 14.5px; letter-spacing: 1.5px; color: var(--dark); }
  .quick-links { position: absolute; left: 398px; top: 2010px; list-style: none; font-size: 11px; line-height: 24px; color: var(--dark); }
  .news-text { position: absolute; left: 575px; top: 2008px; width: 260px; font-size: 11px; line-height: 24px; color: var(--dark); }
  .news-input { position: absolute; left: 573px; top: 2074px; width: 251px; height: 40px; background: var(--white); border: 1px solid var(--rule); border-radius: 3px; font-size: 11px; color: var(--dark); padding-left: 15px; line-height: 38px; }
  .contact-list { position: absolute; left: 904px; top: 2010px; list-style: none; font-size: 11px; color: var(--dark); }
  .contact-list li { display: flex; align-items: flex-start; gap: 12px; line-height: 16px; margin-bottom: 11px; width: 170px; }
  .contact-list svg { flex: none; margin-top: 2px; }
  .contact-list .mail { text-decoration: underline; }
  .footer-rule { position: absolute; left: 132px; top: 2197px; width: 937px; height: 1px; background: var(--rule); }
  .copyright { position: absolute; left: 0; top: 2215px; width: 1200px; text-align: center; font-size: 11px; color: var(--text); }
</style>
</head>
<body>

<header class="site-header">
  <div class="brand"><span class="name">Elena<br>Marlowe</span><span class="sub">FOUNDATION</span></div>
  <div class="social-top"><span></span><span></span><span></span></div>
  <nav class="main-nav">
    <a class="active" style="left:555px">HOME</a>
    <a style="left:653px">ABOUT US</a>
    <a style="left:776px">SERVICES</a>
    <a style="left:895px">NEWS</a>
    <a style="left:987px">CONTACT US</a>
  </nav>
  <div class="nav-underline"></div>
</header>

<section class="hero" role="img" aria-label="Smiling student in a teal cardigan reading a book, classmates blurred in the background">
  <h1 class="hero-title" style="font-weight:400"><span class="l1">SCHOLARSHIPS TO</span><span class="l2">HIGH SCHOOL STUDENTS</span></h1>
  <div class="hero-btn">VIEW DETAILS</div>
  <div class="hero-dots"><span></span><span></span><span></span></div>
</section>

<h2 class="section-title" style="top:650px;font-weight:400">WELCOME TO ELENA MARLOWE</h2>
<p class="welcome-text">Nemo enim ipsam voluptatem quia voluptas sit aspernatur aut odit aut fugit, sed quia consequuntur magni dolores eos qui ratione voluptatem sequi nesciunt. Neque porro quisquam est, qui dolorem ipsum quia dolor sit amet, consectetur, adipisci velit, sed quia non numquam eius modi tempora incidunt ut labore et dolore magnam aliquam quaerat voluptatem.</p>
<div class="btn-small" style="left:547px;top:827px;width:105px;height:36px">READ MORE</div>

<div class="services-band"></div>
<h2 class="section-title" style="top:1004px;font-weight:400">OUR SERVICES</h2>

<div class="service" style="left:132px">
  <svg width="44" height="38" viewBox="0 0 44 38"><rect x="2" y="2" width="40" height="26" rx="2" fill="none" stroke="#8a8a8a" stroke-width="4"/><rect x="17" y="28" width="10" height="6" fill="#8a8a8a"/><rect x="10" y="33" width="24" height="4" fill="#8a8a8a"/></svg>
  <h3>SCHOLARSHIP</h3>
  <p>Nemo enim ipsam voluptatem quia voluptas sit aspernatur aut odit aut fugit, sed quia consequuntur magni dolores</p>
  <span class="more">READ MORE&raquo;</span>
</div>
<div class="service" style="left:458px">
  <svg width="38" height="38" viewBox="0 0 38 38"><path d="M10 3h24l-6 30H4z" fill="#8a8a8a"/><path d="M13 9h15M12 15h15M11 21h15" stroke="#f7f7f7" stroke-width="2"/><path d="M4 33h24" stroke="#f7f7f7" stroke-width="2"/></svg>
  <h3>SCHOOL</h3>
  <p>Nemo enim ipsam voluptatem quia voluptas sit aspernatur aut odit aut fugit, sed quia consequuntur magni dolores</p>
  <span class="more">READ MORE&raquo;</span>
</div>
<div class="service" style="left:786px">
  <svg width="52" height="38" viewBox="0 0 52 38"><path d="M26 4 50 14 26 24 2 14z" fill="#8a8a8a"/><path d="M13 19v10c6 5 20 5 26 0V19l-13 6z" fill="#8a8a8a"/><path d="M46 16v12" stroke="#8a8a8a" stroke-width="2"/></svg>
  <h3>COLLEGE</h3>
  <p>Nemo enim ipsam voluptatem quia voluptas sit aspernatur aut odit aut fugit, sed quia consequuntur magni dolores</p>
  <span class="more">READ MORE&raquo;</span>
</div>

<h2 class="section-title" style="top:1498px;font-weight:400">TESTIMONIALS</h2>

<div class="testimonial" style="left:132px">
  <p>Nemo enim ipsam voluptatem quia voluptas sit aspernatur aut odit aut fugit, sed quia consequuntur magni dolores eos qui ratione voluptatem sequi nesciunt. Neque porro quisquam est, qui dolorem ipsum quia dolor sit amet, consectetur, adipisci velit, sed quia</p>
  <span class="author">- Ana Ruiz -</span>
</div>
<div class="avatar" style="left:441px;top:1746px" role="img" aria-label="Portrait photo of a smiling young woman"></div>

<div class="testimonial" style="left:612px">
  <p>Nemo enim ipsam voluptatem quia voluptas sit aspernatur aut odit aut fugit, sed quia consequuntur magni dolores eos qui ratione voluptatem sequi nesciunt. Neque porro quisquam est, qui dolorem ipsum quia dolor sit amet, consectetur, adipisci velit, sed quia</p>
  <span class="author">- Ana Ruiz -</span>
</div>
<div class="avatar" style="left:921px;top:1746px" role="img" aria-label="Portrait photo of a smiling young man"></div>

<footer class="site-footer"></footer>
<div class="footer-brand"><span class="name">Elena<br>Marlowe</span><span class="sub">FOUNDATION</span></div>
<div class="social-foot"><span></span><span></span><span></span><span></span><span></span></div>

<h4 class="footer-heading" style="left:396px;font-weight:400">QUICK LINKS</h4>
<ul class="quick-links">
  <li>Home</li><li>About us</li><li>Services</li><li>Gallery</li><li>Contact us</li>
</ul>

<h4 class="footer-heading" style="left:572px;font-weight:400">NEWSLETTER</h4>
<p class="news-text">Enter your email address to receive the latest news and notes from our blog.</p>
<div class="news-input">Enter Your Mail Id</div>
<div class="btn-small" style="left:576px;top:2134px;width:82px;height:28px;font-size:10.5px">SUBSCRIBE</div>

<h4 class="footer-heading" style="left:904px;font-weight:400">CONTACT US</h4>
<ul class="contact-list">
  <li><svg width="12" height="11" viewBox="0 0 12 11"><path d="M1 4c0-3 10-3 10 0v1H8V3H4v2H1z M2 6h8l1 4H1z" fill="#555"/></svg>(555) 014-2290</li>
  <li><svg width="12" height="11" viewBox="0 0 12 11"><rect x="3" y="0" width="6" height="3" fill="#555"/><rect x="0" y="3" width="12" height="5" fill="#555"/><rect x="3" y="7" width="6" height="4" fill="#555"/></svg>(555) 014-2290</li>
  <li><svg width="12" height="10" viewBox="0 0 12 10"><rect x="0" y="1" width="12" height="8" fill="#555"/><path d="M0 1l6 4 6-4" stroke="#f7f7f7" fill="none"/></svg><span class="mail">hello@marlowefund.org</span></li>
  <li><svg width="12" height="13" viewBox="0 0 12 13"><path d="M6 12C2 7 1 6 1 4.5a5 5 0 0 1 10 0C11 6 10 7 6 12z" fill="#555"/><circle cx="6" cy="4.5" r="1.7" fill="#f7f7f7"/></svg>#2868 Lorem ipsum dolor sit amet, consectetur</li>
</ul>

<div class="footer-rule"></div>
<p class="copyright">&copy;2017 Fundraising foundation.. All Rights Reserved.</p>

</body>
</html>
```